Mobile mechanics business card

i need a business card for my new business im a mobile mechanic who works on farm machines, ie tractors and construction machines ie bulldozers and frost protection wind machines in orchards so would like those three machines in the back ground to show the customers what i am specializing in. just go for it and suprise me!!

Target Market(s)

orchard owner, farm owners and contractors

Industry/Entity Type

Construction

Contact Information for Business Card

Rob carsley, mobile mechanic, Ph 0264830519, Email robk.carsley47@maplenest.com

```html
<!DOCTYPE html>
<html lang="en">
<head>
<meta charset="utf-8">
<title>Rob Carsley – Mobile Mechanic</title>
<link rel="stylesheet" href="https://fonts.googleapis.com/css2?family=Alfa+Slab+One&family=Lora:wght@700&display=swap">
<style>
  :root {
    --page: #ffffff;
    --card: #ffffff;
    --card-edge: #222222;
    --card-shadow: #bdbdbd;
    --band-grey: #3d3a3a;
    --band-navy: #02021f;
    --band-olive-dark: #2d2a0b;
    --band-olive: #8e8a33;
    --name-red: #e0301e;
    --name-outline: #ffffff;
    --title-magenta: #e0068a;
    --phone-green: #00a651;
    --email-indigo: #3a2d91;
    --dots-grey: #b4b4b4;
    --grass-dark: #3a3432;
  }
  html, body {
    margin: 0;
    width: 1200px;
    height: 675px;
    overflow: hidden;
    background: var(--page);
  }
  .canvas {
    position: relative;
    width: 1200px;
    height: 675px;
  }
  .business-card {
    position: absolute;
    left: 40px;
    top: 18px;
    width: 1122px;
    height: 640px;
    background: var(--card);
    border: 1px solid var(--card-edge);
    box-shadow: 5px 5px 0 var(--card-shadow);
    overflow: hidden;
  }
  .header-band {
    position: absolute;
    left: 0;
    top: 0;
    width: 100%;
    height: 170px;
    display: block;
  }
  .owner-name {
    position: absolute;
    left: 0;
    right: 0;
    top: 46px;
    margin: 0;
    text-align: center;
    font-family: "Alfa Slab One", serif;
    font-weight: 400;
    font-size: 80px;
    line-height: 1;
    letter-spacing: 3px;
    color: var(--name-red);
    -webkit-text-stroke: 2px var(--name-red);
    text-shadow:
      3px 0 0 var(--name-outline), -3px 0 0 var(--name-outline),
      0 3px 0 var(--name-outline), 0 -3px 0 var(--name-outline),
      2px 2px 0 var(--name-outline), -2px -2px 0 var(--name-outline),
      2px -2px 0 var(--name-outline), -2px 2px 0 var(--name-outline),
      0 0 2px #000000;
  }
  .dot-field {
    position: absolute;
    top: 170px;
    width: 300px;
    height: 320px;
  }
  .dot-field--left {
    left: 0;
    background: linear-gradient(200deg, rgba(180,180,180,0.35) 0%, rgba(180,180,180,0.12) 55%, rgba(255,255,255,0) 75%);
    clip-path: polygon(0 0, 100% 0, 0 100%);
  }
  .dot-field--right {
    right: 0;
    background: linear-gradient(160deg, rgba(180,180,180,0.12) 0%, rgba(180,180,180,0.35) 60%, rgba(255,255,255,0) 100%);
    clip-path: polygon(0 0, 100% 0, 100% 100%);
  }
  .contact-line {
    position: absolute;
    left: 0;
    right: 0;
    margin: 0;
    text-align: center;
    font-family: "Lora", serif;
    font-weight: 700;
    line-height: 1;
  }
  .trade-title {
    top: 211px;
    font-size: 60px;
    color: var(--title-magenta);
  }
  .phone-line {
    top: 329px;
    font-size: 46px;
    color: var(--phone-green);
  }
  .email-line {
    top: 427px;
    font-size: 45px;
    color: var(--email-indigo);
  }
  .grass-strip {
    position: absolute;
    left: 0;
    bottom: 0;
    width: 100%;
    height: 130px;
    background: linear-gradient(to bottom, rgba(255,255,255,0) 0%, rgba(150,140,138,0.45) 45%, var(--grass-dark) 100%);
  }
</style>
</head>
<body>
<main class="canvas">
  <section class="business-card">
    <svg class="header-band" viewBox="0 0 1277 193" preserveAspectRatio="none" aria-hidden="true">
      <rect width="1277" height="193" fill="var(--band-grey)"/>
      <polygon points="185,0 390,0 700,193 505,193" fill="var(--band-navy)"/>
      <polygon points="228,0 250,0 560,193 538,193" fill="var(--band-grey)"/>
      <polygon points="645,0 1100,0 1277,110 1277,193 950,193" fill="var(--band-olive-dark)"/>
      <polygon points="760,0 960,0 1250,193 1055,193" fill="var(--band-olive)"/>
    </svg>
    <h1 class="owner-name">ROB CARSLEY</h1>

    <div class="dot-field dot-field--left" role="img" aria-label="Fan of small grey squares radiating from the top left"></div>
    <div class="dot-field dot-field--right" role="img" aria-label="Fan of small grey squares radiating from the top right"></div>

    <p class="contact-line trade-title">Mobile Mechanic</p>
    <p class="contact-line phone-line">Phone : 0264830519</p>
    <p class="contact-line email-line">E-mail : robk.carsley47@maplenest.com</p>

    <div class="grass-strip" role="img" aria-label="Silhouettes of dry grass and weeds along the bottom edge"></div>
  </section>
</main>
</body>
</html>
```